Finance Company Needs a New Website Design

Looking for a fresh new design, based on logo and wireframes given, to come up with a modern professional look and feel for the company. Note we will award based on the homepage design, but expect the winning designer to deliver the other pages.

Target Market(s)

Large Corporate and Finance Professionals (C-Suite Level)

Industry/Entity Type

Finance / Professional

Number of Pages Required

5+ page

Font styles to use
Sans Serif
Other font styles liked:
• Use Roboto/Open Sans for body/small headings, use Impact for larger headings (like the Trevam website).

Requirements
Must have
• High Attention to Detail. Following the Wireframes closely. High impact and fits well with the Trevam.co.uk website.
Nice to have
• Must fit with the Trevam website look and feel, but be different - so that they cannot be mistaken for each other. Use the arrow motif from the logo carefully.
Should not have
• Anything cheap, too bright or untidy

```html
<!DOCTYPE html>
<html lang="en">
<head>
<meta charset="utf-8">
<title>Keystead – Sell Your Business</title>
<link href="https://fonts.googleapis.com/css2?family=Open+Sans:wght@400;600;700;800&display=swap" rel="stylesheet">
<style>
:root{
  --purple:#4b1d5f;
  --purple-deep:#3a1449;
  --grey-dark:#5f5f60;
  --grey-btn:#6a6a6b;
  --grey-light:#ececed;
  --grey-line:#d6d6d8;
  --text:#3b3b3d;
  --white:#ffffff;
}
*{box-sizing:border-box;margin:0;padding:0}
html,body{width:1200px;height:4800px;overflow:hidden}
body{position:relative;background:var(--white);font-family:"Open Sans",Arial,sans-serif;color:var(--text)}
.abs{position:absolute}
p{font-size:11.5px;line-height:1.45;margin-bottom:11px}
a{color:var(--purple)}
.heading{font-weight:700;color:var(--purple);letter-spacing:2px;text-transform:uppercase;line-height:1.2}
.heading.lg{font-size:25px}
.heading.xl{font-size:31px}
.center{text-align:center}
.btn{display:inline-flex;align-items:center;gap:7px;height:30px;padding:0 17px;font-size:9.5px;font-weight:600;letter-spacing:.6px;color:var(--white);text-transform:uppercase;background:var(--purple);border-radius:2px;box-shadow:0 2px 4px rgba(0,0,0,.25)}
.btn.grey{background:var(--grey-btn)}
.btn svg{width:9px;height:11px}
.photo{box-shadow:0 3px 10px rgba(0,0,0,.3)}

/* header */
.site-header{left:0;top:0;width:1200px;height:88px;background:var(--white)}
.brand{left:149px;top:12px;font-size:52px;font-weight:700;color:var(--grey-dark);letter-spacing:-2px;line-height:1}
.top-nav{right:150px;top:16px;display:flex;align-items:center;gap:18px;font-size:9.5px;color:#777;text-transform:uppercase}
.phone-pill{display:flex;align-items:center;gap:8px;background:#eee;padding:5px 10px;font-size:13px;color:var(--text)}
.phone-icon{width:20px;height:20px;background:var(--purple);border-radius:3px;display:flex;align-items:center;justify-content:center}
.main-nav{right:150px;top:52px;display:flex;gap:32px;font-size:14px;color:var(--purple);text-transform:uppercase;letter-spacing:.4px}
.main-nav .current{color:var(--grey-dark);text-decoration:underline}

/* hero */
.hero{left:0;top:88px;width:1200px;height:500px;background:linear-gradient(90deg,#2a2c2f 0%,#3a3d41 40%,#55595e 70%,#6b6f74 100%)}
.hero-copy{left:190px;top:282px;width:310px;color:var(--white);text-align:center;font-size:38px;line-height:1.14;letter-spacing:1px}
.hero-copy b{font-weight:700}
.hero-copy span{font-weight:400}

/* sell */
.sell-mark{left:244px;top:662px;width:164px;height:234px;background:var(--purple)}
.sell-copy{left:474px;top:656px;width:520px}
.sell-copy .heading{margin-bottom:18px}

/* reach */
.reach-copy{left:149px;top:1053px;width:410px}
.reach-copy .heading{margin-bottom:18px}

/* connect */
.connect-copy{left:641px;top:1504px;width:408px}
.connect-copy .heading{margin-bottom:18px}

/* contact band */
.contact-band{left:0;top:2223px;width:1200px;height:435px;background:linear-gradient(90deg,#e9e6e0 0%,#f6f5f2 35%,#f1efeb 60%,#d9d4cc 100%)}
.contact-copy{left:280px;top:2362px;width:350px}

/* articles */
.card{width:210px;height:252px}
.card-img{width:210px;height:186px}
.card-cap{position:absolute;left:10px;right:10px;top:172px;padding:12px 8px;background:var(--white);font-size:11px;line-height:1.35;text-align:center;color:var(--text);box-shadow:0 2px 5px rgba(0,0,0,.15)}
.card-cap.active{background:var(--grey-btn);color:var(--white)}

/* footer */
.offices{left:149px;top:4290px;width:902px;height:233px;background:var(--white);box-shadow:0 2px 6px rgba(0,0,0,.15)}
.office-label{font-size:12.5px;font-weight:700;color:var(--purple);letter-spacing:.8px;margin-bottom:20px}
.office-addr{font-size:10.5px;line-height:1.75}
.office-phone{display:flex;align-items:center;gap:9px;font-size:12px}
.foot-col h4{font-size:10.5px;font-weight:700;color:var(--purple);letter-spacing:.5px;margin-bottom:10px;text-transform:uppercase}
.foot-col li{list-style:none;font-size:10.5px;line-height:1.95;color:var(--text)}
.foot-brand{left:200px;top:4590px;font-size:46px;font-weight:700;color:var(--purple);line-height:.95;letter-spacing:-2px}
.alert-input{left:390px;top:4680px;width:330px;height:30px;background:var(--white);border:1px solid var(--grey-line);font-size:10px;color:#aaa;padding:8px 36px}
.alert-btn{left:720px;top:4680px;width:106px;height:30px;justify-content:center}
.bottom-bar{left:0;top:4772px;width:1200px;height:28px;background:var(--purple);color:var(--white);font-size:9.5px;display:flex;align-items:center;justify-content:space-between;padding:0 90px 0 149px}
.bottom-bar nav{display:flex;gap:14px}
</style>
</head>
<body>

<!-- header -->
<header class="site-header abs">
  <div class="brand abs">keystead</div>
  <div class="top-nav abs">
    <span>Insights &amp; News</span><span>About Us</span><span>Contact Us</span>
    <span class="phone-pill"><span class="phone-icon"><svg width="11" height="11" viewBox="0 0 24 24"><path fill="#fff" d="M6.6 10.8a15 15 0 006.6 6.6l2.2-2.2a1 1 0 011-.25 11 11 0 003.6.57 1 1 0 011 1V20a1 1 0 01-1 1A17 17 0 013 4a1 1 0 011-1h3.5a1 1 0 011 1 11 11 0 00.57 3.6 1 1 0 01-.25 1z"/></svg></span>0333 010 4470</span>
  </div>
  <nav class="main-nav abs"><span class="current">Sell Your Business</span><span>Valuation</span><span>Work With Us</span></nav>
</header>

<!-- hero -->
<section class="hero abs" role="img" aria-label="Photograph of a heavy steel bank vault door set into a dark concrete wall"></section>
<div class="hero-copy abs"><span>WE FIND </span><b>THE<br>BEST BUYER</b><br><span>YOU GET </span><b>THE<br>BEST EXIT</b></div>
<svg class="abs" style="left:0;top:500px" width="1200" height="100" viewBox="0 0 1200 100">
  <path d="M0 0 L0 100 L1200 100 L1200 0 C1150 20 1110 70 1060 72 L60 72 C40 72 20 40 0 0Z" fill="#fff"/>
  <path d="M0 8 C20 45 40 72 70 72 L1060 72 C1110 70 1150 30 1200 6 L1200 18 C1150 40 1110 82 1060 84 L70 84 C40 84 20 60 0 28Z" fill="var(--purple)"/>
</svg>

<!-- sell your business -->
<div class="sell-mark abs" aria-hidden="true"></div>
<div class="sell-copy abs">
  <h1 class="heading lg">Sell Your Business For More</h1>
  <p>You may have already considered how much your business is worth, or even have received a suggested price for the sale of your business. If you have, then it might be worth considering a very apparent truth.</p>
  <p>Any business valuation you have in mind, or have received, is just a number. In many cases, it is not close to what your business may sell for. To wish is one thing, to receive a good offer is much harder.</p>
  <p>Which is why owners choose to work with us. We know that your future business disposal and sale price will be maximised in two ways: by <a href="#">reaching as many of the most likely buyers</a> as possible, and by <a href="#">finding the best fit</a>.</p>
  <p>Only then will you receive the best offer for your business and complete on the disposal of your company.</p>
</div>

<!-- reach section background -->
<svg class="abs" style="left:0;top:938px" width="1200" height="492" viewBox="0 0 1200 492">
  <path d="M0 0 L40 20 L1200 20 L1200 462 L1060 462 L1030 440 L990 440 L1000 492 L0 462Z" fill="var(--grey-light)"/>
</svg>
<div class="reach-copy abs">
  <h2 class="heading lg">Reach Only<br>Serious Acquirers</h2>
  <p>With access to over 13,000 active acquirers throughout our national and global network, all of whom we have qualified to ensure they have the capabilities to make good offers for suitable businesses.</p>
  <p>We have partnerships with websites we have evaluated to give us the greatest possible coverage of any additional buyers who may be interested in your company.</p>
  <p>We have a full set of global business data meaning that we can run intensive campaigns to help you get in front of specific trade buyers, and with our office in Sydney, we cover every time zone.</p>
  <span class="btn" style="margin-top:8px">Reach Matters <svg viewBox="0 0 9 11"><path d="M4.5 0L9 5H6v6H3V5H0z" fill="#fff"/></svg></span>
</div>
<div class="abs photo" style="left:628px;top:1058px;width:422px;height:280px;background:linear-gradient(135deg,#0c2c5c,#1f5fa3 55%,#0a1f45)" role="img" aria-label="Photograph of a hand pointing at a glowing upward arrow over blue financial charts"></div>

<!-- connect -->
<div class="abs photo" style="left:149px;top:1496px;width:423px;height:317px;background:linear-gradient(135deg,#1e1e20,#2d2b2e 60%,#3a3234)" role="img" aria-label="Photograph of hands fitting colourful jigsaw puzzle pieces together on a dark surface"></div>
<div class="connect-copy abs">
  <h2 class="heading lg">Connect With The<br>Best Fitting Buyers</h2>
  <p>From our research, and having engaged with as many potential acquirers as possible, we will work alongside you to identify the most interesting prospective acquirers.</p>
  <p>In most cases these are the companies with the best fit for your business. It will mean that they will pay a premium for your business because there is more value.</p>
  <p>Working with you, we will coordinate a competitive process, engaging the most suitable acquirers and their advisors, and ensuring that the offers made exceed expectations, not just in price, but also in terms of your future.</p>
  <span class="btn grey" style="margin-top:8px">Finding The Fit <svg viewBox="0 0 9 11"><path d="M4.5 0L9 5H6v6H3V5H0z" fill="#fff"/></svg></span>
</div>

<!-- contact band -->
<div class="contact-band abs" role="img" aria-label="Photograph of a smiling businessman in a suit reaching out for a handshake in a bright office"></div>
<div class="abs photo" style="left:255px;top:1878px;width:690px;height:380px;background:linear-gradient(135deg,#0b2326,#17484c 50%,#0d2a2e)" role="img" aria-label="Video still of a finger touching a tablet showing a glowing line chart"></div>
<svg class="abs" style="left:572px;top:2041px" width="56" height="56" viewBox="0 0 56 56"><circle cx="28" cy="28" r="26" fill="var(--purple)" stroke="#fff" stroke-width="2"/><path d="M22 17L40 28L22 39Z" fill="#fff"/></svg>
<div class="contact-copy abs center">
  <h2 class="heading xl" style="margin-bottom:18px">Contact The<br>Keystead Team</h2>
  <p style="font-size:12px">Book an introductory call with one of our team and discover first hand how Keystead can realise a successful sale of your company</p>
  <div style="display:flex;gap:10px;justify-content:center;margin-top:18px">
    <span class="btn" style="font-size:12px;text-transform:none;letter-spacing:0"><svg viewBox="0 0 24 24" style="width:12px;height:12px"><path fill="#fff" d="M6.6 10.8a15 15 0 006.6 6.6l2.2-2.2a1 1 0 011-.25 11 11 0 003.6.57 1 1 0 011 1V20a1 1 0 01-1 1A17 17 0 013 4a1 1 0 011-1h3.5a1 1 0 011 1 11 11 0 00.57 3.6 1 1 0 01-.25 1z"/></svg>0333 010 4470</span>
    <span class="btn grey">Contact Keystead <svg viewBox="0 0 9 11"><path d="M4.5 0L9 5H6v6H3V5H0z" fill="#fff"/></svg></span>
  </div>
</div>

<!-- valuations -->
<div class="abs center" style="left:290px;top:2730px;width:620px">
  <h2 class="heading lg" style="margin-bottom:22px">Business Valuations Based<br>On Real Transaction Data</h2>
  <p>Business valuation is the most misunderstood part of the disposal process and often comes before engaging an advisor. Yet, all this does is raise more questions. Why be distracted by hope or hearsay when there is so much information available?</p>
  <p>We have been directly involved in a wide range of transactions, and have also access to deal data from over 1,000 recent business disposals. So we are confident that we have access to enough information to give a more representative view on valuation.</p>
  <p>So, you can browse our statistics on valuation to give a much clearer picture of business value, or use our calculator to get an idea of a starting point for your business value.</p>
  <div style="display:flex;gap:10px;justify-content:center;margin-top:20px">
    <span class="btn">Business Sale Data <svg viewBox="0 0 9 11"><path d="M4.5 0L9 5H6v6H3V5H0z" fill="#fff"/></svg></span>
    <span class="btn grey">Valuation Calculator <svg viewBox="0 0 9 11"><path d="M4.5 0L9 5H6v6H3V5H0z" fill="#fff"/></svg></span>
  </div>
</div>

<!-- articles -->
<svg class="abs" style="left:0;top:3052px" width="1200" height="500" viewBox="0 0 1200 500">
  <path d="M0 0 L160 0 L190 22 L1200 22 L1200 498 L1050 498 L1010 470 L0 470Z" fill="var(--grey-light)"/>
</svg>
<h2 class="heading lg abs center" style="left:0;top:3162px;width:1200px">Articles And Insights</h2>
<div class="card abs" style="left:149px;top:3217px"><div class="card-img" style="background:linear-gradient(135deg,#e8e4de,#c9c2b8)" role="img" aria-label="Photograph of a delighted woman at a laptop"></div><div class="card-cap">You Can Pursue Your<br>Own Business Sale</div></div>
<div class="card abs" style="left:380px;top:3217px"><div class="card-img" style="background:linear-gradient(135deg,#d5d2cd,#9a958f)" role="img" aria-label="Photograph of two businessmen reviewing a tablet together"></div><div class="card-cap">Gain a Full Understanding<br>of What Your Sale Advisor<br>is Offering</div></div>
<div class="card abs" style="left:610px;top:3217px"><div class="card-img" style="background:linear-gradient(135deg,#cfd3d6,#6e757b)" role="img" aria-label="Photograph of two men in suits in conversation"></div><div class="card-cap active">It's Too Easy to Believe<br>the Largest Figure</div></div>
<div class="card abs" style="left:841px;top:3217px"><div class="card-img" style="background:linear-gradient(135deg,#eceae6,#b7b3ad)" role="img" aria-label="Photograph of a man crossing his arms in a refusal gesture"></div><div class="card-cap">Don't Be Your Own<br>Worst Enemy</div></div>

<!-- reach worldwide -->
<div class="abs center" style="left:290px;top:3628px;width:620px">
  <h2 class="heading lg" style="margin-bottom:18px">Local And International Reach</h2>
  <p>Our focus on technology, business data and modern communications sets us apart. Borders and languages aren't boundaries for the way we operate.</p>
  <p>Our methods are successful whether helping a company sell within a small region, or cross-border, or even cross-continent.</p>
</div>
<div class="abs" style="left:265px;top:3754px;width:668px;height:397px;border:1px solid var(--grey-line);background:radial-gradient(ellipse at 50% 45%,#dfe3e6 0%,#eef0f2 55%,#fff 80%)" role="img" aria-label="World map with North America, Europe, India and Australia highlighted in purple"></div>

<!-- footer -->
<svg class="abs" style="left:0;top:4212px" width="1200" height="588" viewBox="0 0 1200 588">
  <path d="M0 60 C40 40 70 10 110 10 L1200 10 L1200 588 L0 588Z" fill="var(--grey-light)"/>
  <path d="M0 50 C40 28 70 0 110 0 L1200 0 L1200 10 L110 10 C70 10 40 40 0 62Z" fill="var(--purple)"/>
</svg>
<div class="offices abs">
  <div class="abs" style="left:18px;top:20px">
    <div class="office-label">EUROPE &amp; UK OFFICE:</div>
    <div class="office-addr">Second Floor<br>Millbank Court<br>Reading<br>RG1 4ZZ</div>
  </div>
  <div class="office-phone abs" style="left:22px;top:200px"><span class="phone-icon"><svg width="11" height="11" viewBox="0 0 24 24"><path fill="#fff" d="M6.6 10.8a15 15 0 006.6 6.6l2.2-2.2a1 1 0 011-.25 11 11 0 003.6.57 1 1 0 011 1V20a1 1 0 01-1 1A17 17 0 013 4a1 1 0 011-1h3.5a1 1 0 011 1 11 11 0 00.57 3.6 1 1 0 01-.25 1z"/></svg></span>0333 010 4470</div>
  <div class="abs" style="left:200px;top:0;width:254px;height:233px;background:linear-gradient(135deg,#eef0ea,#dde3e6)" role="img" aria-label="Street map of central Reading with office location pin"></div>
  <div class="abs" style="left:461px;top:0;width:254px;height:233px;background:linear-gradient(135deg,#edf0ec,#dce2e8)" role="img" aria-label="Street map of Barangaroo, Sydney with office location pin"></div>
  <div class="abs" style="right:18px;top:20px;text-align:right">
    <div class="office-label">APAC OFFICE:</div>
    <div class="office-addr">12 Harbour Lane<br>Barangaroo<br>NSW 2000<br>Australia</div>
  </div>
  <div class="office-phone abs" style="right:22px;top:200px"><span class="phone-icon"><svg width="11" height="11" viewBox="0 0 24 24"><path fill="#fff" d="M6.6 10.8a15 15 0 006.6 6.6l2.2-2.2a1 1 0 011-.25 11 11 0 003.6.57 1 1 0 011 1V20a1 1 0 01-1 1A17 17 0 013 4a1 1 0 011-1h3.5a1 1 0 011 1 11 11 0 00.57 3.6 1 1 0 01-.25 1z"/></svg></span>+61 (0) 400 128 360</div>
</div>

<div class="foot-brand abs">key<br>stead</div>
<div class="foot-col abs" style="left:390px;top:4566px"><h4>Sell Your Business</h4><ul><li style="text-decoration:underline">Direct to Market</li><li>Maximising Reach</li><li>Focus on Fit</li><li>Exit Planning</li></ul></div>
<div class="foot-col abs" style="left:588px;top:4566px"><h4>Valuation</h4><ul><li>Calculator</li><li>Getting the Fit</li><li>How to Build Value</li></ul></div>
<div class="foot-col abs" style="left:754px;top:4566px"><h4>Work With Us</h4><ul><li>M&amp;A Advisors</li><li>Global Coverage</li><li>Acquisitions</li></ul></div>
<div class="foot-col abs" style="left:911px;top:4566px"><h4>About Us</h4><ul><li>Insights and News</li><li>About Us</li><li>Contact Us</li></ul></div>

<div class="alert-input abs">email address</div>
<svg class="abs" style="left:400px;top:4689px" width="16" height="12" viewBox="0 0 16 12"><rect x=".5" y=".5" width="15" height="11" fill="none" stroke="#bbb"/><path d="M.5.5L8 7l7.5-6.5" fill="none" stroke="#bbb"/></svg>
<span class="btn alert-btn abs">Get Alert</span>

<footer class="bottom-bar abs">
  <span>© 2023 Keystead. All Right Reserved</span>
  <nav><span>Sitemap</span><span>Terms of Use</span><span>Privacy Policy</span><span>Contact Us</span></nav>
</footer>

</body>
</html>
```